Quillbrook Health needs a new services brochure

We need a new brochure that highlights the services that we offer at our clinic. We are a multidisciplinary health clinic that focuses on injury rehabilitation and pain management. We are looking for a brochure that will highlight our primary services to our clientele and inform potential clients of what we can offer. We pride ourselves on our quality of care and our advanced treatment techniques.
Target Market(s)
young families, athletes, people interested in their health.
Industry/Entity Type
Health And Wellness
Colors
Designer to choose colors to be used in the design.
Requirements
Must have
- We would love our new brochure to be a tri-fold that has 6 pages. We would like it to have brief information about our featured services:
- - Chiropractic
- - Massage Therapy
- - Manual Osteopathic Therapy
- - Acupuncture
- - Laser Therapy
- - Radial Shockwave Therapy
- We would also like this brochure to include a brief price list and direct billing info, About Us section & Contact information.
Nice to have
- If there is space to list that we also offer other services such as : Tissue Unwind Method, Hot Stone Massage, Cupping Technique, Pembrill Method, and Kinesiology Taping that would be great. We would like to use images similar to those that are on our website (we have hi-res of all images on the website) www.quillbrookhealth.ca and colours that would fit with our logo.

```html
<!DOCTYPE html>
<html lang="en">
<head>
<meta charset="utf-8">
<title>Quillbrook Health – Services Brochure</title>
<link href="https://fonts.googleapis.com/css2?family=Open+Sans:wght@400;600;700&family=Source+Sans+3:wght@400;600;700&display=swap" rel="stylesheet">
<style>
:root{
  --blue:#1c5eaa;
  --blue-deep:#123d78;
  --orange:#f47b20;
  --ink:#3d3d3d;
  --paper:#ffffff;
  --backdrop:#d6d7da;
  --body:"Source Sans 3",Arial,sans-serif;
  --head:"Open Sans",Arial,sans-serif;
}
*{margin:0;padding:0;box-sizing:border-box}
html,body{width:869px;height:1200px;overflow:hidden;background:var(--backdrop)}
.stage{position:absolute;left:0;top:0;width:980px;height:1354px;transform:scale(.88673);transform-origin:0 0;font-family:var(--body);color:var(--ink)}
.sheet{position:absolute;left:72px;width:843px;height:595px;background:var(--paper);box-shadow:4px 6px 10px rgba(0,0,0,.35);overflow:hidden}
.sheet--outside{top:57px}
.sheet--inside{top:708px}
.abs{position:absolute}
.photo{position:absolute}
.fold{position:absolute;top:0;width:1px;height:100%;background:rgba(0,0,0,.12)}
.pill{position:absolute;height:27px;display:flex;align-items:center;font-family:var(--head);font-weight:600;font-size:17px;color:#fff;letter-spacing:.3px}
.pill--tab{left:0;width:168px;background:var(--blue);border-radius:0 14px 14px 0;padding-left:18px}
.pill--orange{background:var(--orange);border-radius:14px;justify-content:center}
.btn{position:absolute;height:28px;border-radius:8px;display:flex;align-items:center;justify-content:center;color:#fff;font-family:var(--head);font-size:14.5px;letter-spacing:.8px}
.btn--blue{background:var(--blue);box-shadow:0 2px 3px rgba(0,0,0,.3)}
.btn--orange{background:var(--orange);box-shadow:0 2px 3px rgba(0,0,0,.3)}
.btn--navy{background:var(--blue-deep);box-shadow:0 2px 3px rgba(0,0,0,.3)}
.body-copy{font-size:10.6px;line-height:13px;text-align:justify}
.wordmark{font-family:var(--head);font-weight:600;letter-spacing:.3px}
.contact-panel{position:absolute;left:281px;top:0;width:280px;height:595px;background:linear-gradient(160deg,#2d78c4 0%,#1c5eaa 45%,#174b90 100%);color:#fff;text-align:center}
.address{font-size:10.8px;line-height:15px}
.hours-title{font-family:var(--head);font-weight:600;font-size:17px}
.hours{position:absolute;left:75px;top:436px;font-size:9.6px;line-height:13px;text-align:left;border-collapse:collapse}
.hours td{padding:0}
.hours td:first-child{width:78px}
.tagline{position:absolute;left:561px;width:282px;text-align:center;font-family:var(--head);font-weight:700;font-size:21px;letter-spacing:.2px;line-height:26px}
.service{position:absolute;width:250px}
.service h3{font-family:var(--head);font-weight:600;font-size:13px;color:#333;line-height:16px}
.service p{font-size:10.5px;line-height:13px;text-align:justify}
.price-panel{position:absolute;left:561px;top:0;width:282px;height:595px;background:linear-gradient(165deg,#1f63b0 0%,#174d92 60%,#123f7a 100%);color:#fff}
.price-group{position:absolute;left:575px;width:258px;color:#fff}
.price-group h4{font-family:var(--head);font-weight:400;font-size:10.5px;letter-spacing:.1px;margin-bottom:4px}
.row{display:flex;align-items:baseline;font-size:7.6px;line-height:11px}
.row .name{white-space:nowrap}
.row .dots{flex:1;border-bottom:1px dotted rgba(255,255,255,.7);margin:0 2px 2px}
.row .p1{width:40px}
.row .p2{width:46px}
.row .note{font-size:4.6px;white-space:nowrap;margin-left:-20px;width:66px}
.price-note{font-size:7.6px;line-height:11px}
.col-heads{position:absolute;top:76px;left:748px;font-size:5px;color:#fff}
.col-heads span{position:absolute;white-space:nowrap}
.hero-title{position:absolute;color:#fff;font-family:var(--head);font-weight:600;font-size:33px;letter-spacing:.5px;text-shadow:0 1px 3px rgba(0,0,0,.35)}
.inset{position:absolute;border-radius:50%;border:3px solid #fff;box-shadow:0 0 0 2px var(--blue)}
</style>
</head>
<body>
<div class="stage">

  <section class="sheet sheet--outside">
    <div class="photo" role="img" aria-label="Clinic reception area with front desk and waiting chairs" style="left:0;top:0;width:281px;height:280px;background:linear-gradient(135deg,#8a7a68 0%,#c9b9a2 40%,#6d6253 75%,#4a4038 100%)"></div>
    <svg class="abs" style="left:0;top:0" width="281" height="300" viewBox="0 0 281 300">
      <path d="M0 0 H30 Q120 30 281 55 V0Z" fill="var(--blue)"/>
      <path d="M0 18 Q150 40 281 52" stroke="var(--orange)" stroke-width="4" fill="none"/>
      <path d="M0 262 Q140 282 281 272 V300 H0Z" fill="#fff"/>
      <path d="M0 262 Q140 282 281 272" stroke="var(--blue)" stroke-width="3" fill="none"/>
    </svg>
    <div class="pill pill--tab" style="top:293px">ABOUT US</div>
    <div class="body-copy abs" style="left:16px;top:330px;width:257px">
      <p>NW Kestrel Bay's Quillbrook Health offers Chiropractic, Massage Therapy, Manual Osteopathy, Acupuncture and more. We are take a comprehensive approach for pain relief and injury recovery to help you get back to enjoying a healthy, active life.</p>
      <p style="margin-top:13px">Our mission is to provide the best rehabilitative solutions to our patients so they can LIVE LIFE pain free.</p>
      <p style="margin-top:26px">We are owner-operated and patient focused. Our treatments are evidence informed (backed by credible scientific research) and everything we offer is covered by extended health insurance. We are located just north off Marlow Trail in Fernhollow, one of NW Kestrel Bay's newest and largest communities.</p>
    </div>
    <div class="btn btn--blue" style="left:27px;top:551px;width:227px">Book Online Now!</div>

    <div class="contact-panel">
      <div class="abs" role="img" aria-label="Street map showing clinic location" style="left:70px;top:41px;width:136px;height:136px;border-radius:50%;background:radial-gradient(circle,#f4f4f2 0%,#e6e8e4 100%);border:3px solid #fff;box-shadow:0 2px 6px rgba(0,0,0,.3)"></div>
      <svg class="abs" style="left:131px;top:86px" width="14" height="20" viewBox="0 0 14 20"><path d="M7 0C3 0 0 3 0 7c0 5 7 13 7 13s7-8 7-13c0-4-3-7-7-7z" fill="#e23b2e"/><circle cx="7" cy="7" r="2.5" fill="#fff"/></svg>
      <div class="abs wordmark" style="left:0;width:280px;top:220px;font-size:24px;display:flex;align-items:center;justify-content:center;gap:8px"><span style="width:11px;height:11px;border-radius:50%;background:#fff;display:inline-block"></span>Quillbrook Health</div>
      <div class="pill pill--orange" style="left:61px;top:293px;width:156px">CONTACT US</div>
      <div class="address abs" style="left:0;width:280px;top:344px">Fernhollow Commons<br>4150 - 1180 Larkspur Valley Rd NW<br>Kestrel Bay, AB T9X 2K4</div>
      <div class="hours-title abs" style="left:0;width:280px;top:409px">HOURS</div>
      <table class="hours">
        <tr><td>Monday</td><td>8am - 9pm</td></tr>
        <tr><td>Tuesday</td><td>8am - 9pm</td></tr>
        <tr><td>Wednesday</td><td>8am - 8pm</td></tr>
        <tr><td>Thursday</td><td>8am - 9pm</td></tr>
        <tr><td>Friday</td><td>8am - 8pm</td></tr>
        <tr><td>Saturday</td><td>9am - 5pm</td></tr>
        <tr><td>Sunday</td><td>10am - 3pm</td></tr>
      </table>
      <div class="btn btn--orange" style="left:26px;top:551px;width:227px">www.quillbrookhealth.ca</div>
    </div>

    <div class="photo" role="img" aria-label="Smiling young family of four outdoors" style="left:561px;top:95px;width:282px;height:370px;background:linear-gradient(160deg,#c9d98a 0%,#a8c46a 35%,#d9a88a 60%,#7aa0c8 100%)"></div>
    <svg class="abs" style="left:281px;top:0" width="562" height="480" viewBox="0 0 562 480">
      <path d="M312 0 H562 V108 Q440 100 380 70 Q330 40 312 0Z" fill="#fff"/>
      <path d="M0 50 Q150 70 280 92 Q450 118 562 95" stroke="var(--orange)" stroke-width="4" fill="none"/>
      <path d="M280 92 Q450 118 562 95 V108 Q440 100 380 70 Q320 35 312 0 L280 0Z" fill="var(--blue)"/>
      <path d="M280 440 Q420 470 562 445 V480 H280Z" fill="#fff"/>
      <path d="M280 440 Q420 470 562 445" stroke="var(--orange)" stroke-width="4" fill="none"/>
    </svg>
    <div class="abs wordmark" style="left:616px;top:40px;font-size:21px;color:var(--blue);display:flex;align-items:center;gap:7px"><span style="width:10px;height:10px;border-radius:50%;background:var(--blue);display:inline-block"></span>Quillbrook Health</div>
    <div class="tagline" style="top:484px;color:var(--blue)">HELPING YOU LIVE LIFE</div>
    <div class="tagline" style="top:510px;color:var(--orange)">PAIN FREE</div>
    <div class="btn btn--navy" style="left:584px;top:551px;width:227px;gap:24px">
      <svg width="20" height="20" viewBox="0 0 20 20"><circle cx="10" cy="10" r="9" fill="none" stroke="#fff" stroke-width="1.4"/><path d="M7 5.5l1.6 2.3-1 1.2c.6 1.3 1.6 2.3 2.9 2.9l1.2-1 2.3 1.6-.8 1.6c-3.6-.3-6.6-3.3-6.9-6.9z" fill="#fff"/></svg>
      <span>(555) 018-4273</span>
    </div>
    <div class="fold" style="left:281px"></div>
    <div class="fold" style="left:561px"></div>
  </section>

  <section class="sheet sheet--inside">
    <div class="photo" role="img" aria-label="Woman jogging along a leafy park path" style="left:0;top:0;width:561px;height:240px;background:linear-gradient(120deg,#c9a27c 0%,#8aa05a 30%,#5f7d3a 60%,#9fb38a 100%)"></div>
    <svg class="abs" style="left:0;top:150px" width="561" height="110" viewBox="0 0 561 110">
      <path d="M0 45 Q60 85 200 78 Q380 68 561 40 V110 H0Z" fill="#fff"/>
      <path d="M0 45 Q60 85 200 78 Q380 68 561 40" stroke="var(--blue)" stroke-width="5" fill="none"/>
    </svg>
    <div class="hero-title" style="left:332px;top:30px">LIVE LIFE</div>
    <div class="hero-title" style="left:360px;top:66px">pain free</div>
    <div class="inset" role="img" aria-label="Shoulder treated with instrument-assisted therapy" style="left:233px;top:138px;width:94px;height:94px;background:linear-gradient(135deg,#caa086,#6b4e3e)"></div>
    <div class="inset" role="img" aria-label="Laser therapy device applied to skin" style="left:341px;top:138px;width:94px;height:94px;background:linear-gradient(135deg,#d8dde2,#4a6a8a)"></div>
    <div class="inset" role="img" aria-label="Therapist massaging a leg" style="left:452px;top:135px;width:100px;height:100px;background:linear-gradient(135deg,#e6cbb5,#b08a70)"></div>

    <div class="pill pill--tab" style="top:246px">OUR SERVICES</div>

    <div class="service" style="left:16px;top:285px"><h3>CHIROPRACTIC</h3><p>Is the assessment, treatment, rehabilitation and prevention of musculoskeletal (bones, muscles, tendons, joints and cartilage) conditions and disorders.</p></div>
    <div class="service" style="left:16px;top:365px"><h3>MASSAGE THERAPY</h3><p>Is the assessment and treatment of the soft tissues of the body, specifically, the muscles, connective tissue, tendons, ligaments and joints for the purpose of optimizing health.</p></div>
    <div class="service" style="left:16px;top:447px"><h3>MANUAL OSTEOPATHIC THERAPY</h3><p>Is the assessment and treatment of all of the components that make up the structure of the human body.</p></div>
    <div class="service" style="left:16px;top:525px"><h3>ACUPUNCTURE</h3><p style="text-align:left">Traditional Chinese Medicine technique to improve the body's functions and natural healing ability.</p></div>

    <div class="service" style="left:296px;top:257px"><h3>LASER THERAPY</h3><p>Is a non-invasive, painless treatment which uses focused light at specific wavelengths to help reduce and often eliminate pain from injuries and chronic conditions.</p></div>
    <div class="service" style="left:296px;top:337px"><h3>RADIAL SHOCKWAVE THERAPY</h3><p style="text-align:left">Is the latest innovation in the treatment of chronic soft tissue injuries.</p></div>
    <div class="service" style="left:296px;top:391px"><h3>PEMBRILL METHOD</h3><p style="text-align:left">Is a form of instrument-assisted soft tissue manipulation.</p></div>
    <div class="service" style="left:296px;top:447px"><h3>CUPPING TECHNIQUE</h3><p>Unlike traditional massage therapy which works to compress tissue and often restrict blood flow, cupping provides negative pressure to skin, muscles and connective tissue.</p></div>
    <div class="service" style="left:296px;top:525px"><h3>HOT STONE MASSAGE</h3><p>Is a form of massage therapy that utilizes hot stones to apply soothing, deep heat to your tissues.</p></div>

    <div class="price-panel">
      <div class="pill pill--orange" style="left:27px;top:16px;width:227px">OUR PRICES</div>
    </div>
    <div class="col-heads"><span style="left:0">Initial</span><span style="left:39px">Subsequent</span></div>

    <div class="price-group" style="top:63px">
      <h4>CHIROPRACTIC</h4>
      <div class="row"><span class="name">Pediatrics 0-5 yr old</span><span class="dots"></span><span class="p1">$115</span><span class="p2">$55</span></div>
      <div class="row"><span class="name">Student ( 6+yrs, full time)</span><span class="dots"></span><span class="p1">$115</span><span class="p2">$55</span></div>
      <div class="row"><span class="name">Adult</span><span class="dots"></span><span class="p1">$125</span><span class="p2">$65</span></div>
      <div class="row"><span class="name">Senior 65+ yrs</span><span class="dots"></span><span class="p1">$115</span><span class="p2">$55</span></div>
      <div class="row"><span class="name">Chiropractic and laser treatment</span><span class="dots"></span><span class="p1"></span><span class="p2">$95</span></div>
      <div class="row"><span class="name">Chiropractic and shockwave therapy</span><span class="dots"></span><span class="p1"></span><span class="p2">$95</span></div>
    </div>
    <div class="price-group" style="top:163px">
      <h4>MASSAGE THERAPY</h4>
      <div class="row"><span class="name">30 Minute</span><span class="dots"></span><span class="p1">$50</span><span class="p2"></span></div>
      <div class="row"><span class="name">45 Minute</span><span class="dots"></span><span class="p1">$75</span><span class="p2"></span></div>
      <div class="row"><span class="name">60 Minutes</span><span class="dots"></span><span class="p1">$90</span><span class="p2"></span></div>
      <div class="row"><span class="name">90 Minutes</span><span class="dots"></span><span class="p1">$130</span><span class="p2"></span></div>
      <div class="row"><span class="name">Infant Massage Instruction</span><span class="dots"></span><span class="p1">$50</span><span class="p2"></span></div>
      <div class="row"><span class="name">Hot Stone Addition</span><span class="dots"></span><span class="p1">+$20</span><span class="p2 note">to regular treatment price</span></div>
    </div>
    <div class="price-group" style="top:261px">
      <h4>MANUAL OSTEOPATHIC THERAPY</h4>
      <div class="row"><span class="name">Initial Assessment and Treatment</span><span class="dots"></span><span class="p1">$150</span><span class="p2"></span></div>
      <div class="row"><span class="name">Subsequent Treatment</span><span class="dots"></span><span class="p1">$120</span><span class="p2"></span></div>
    </div>
    <div class="price-group" style="top:313px">
      <h4>ACUPUNCTURE</h4>
      <div class="row"><span class="name">Initial Assessment and Treatment</span><span class="dots"></span><span class="p1">$120</span><span class="p2"></span></div>
      <div class="row"><span class="name">Subsequent Treatment</span><span class="dots"></span><span class="p1">$85</span><span class="p2"></span></div>
    </div>
    <div class="price-group" style="top:367px">
      <h4>LASER THERAPY</h4>
      <div class="row"><span class="name">Initial Assessment and Treatment</span><span class="dots"></span><span class="p1">$90</span><span class="p2"></span></div>
      <div class="row"><span class="name">Subsequent Treatments</span><span class="dots"></span><span class="p1">$50</span><span class="p2"></span></div>
    </div>
    <div class="price-group" style="top:424px">
      <h4>SHOCKWAVE THERAPY</h4>
      <div class="row"><span class="name">Initial Assessment and Treatment</span><span class="dots"></span><span class="p1">$90</span><span class="p2"></span></div>
      <div class="row"><span class="name">Subsequent Treatments</span><span class="dots"></span><span class="p1">$75</span><span class="p2"></span></div>
    </div>
    <div class="price-group" style="top:479px">
      <h4>CUPPING TECHNIQUE</h4>
      <p class="price-note">Included with massage therapy with Reid and Tessa<br>and acupuncture with Dr. Maren</p>
    </div>
    <div class="price-group" style="top:532px">
      <h4>PEMBRILL METHOD</h4>
      <p class="price-note">Included with chiropractic treatment with Dr. Hollis<br>and Dr. Priya and massage therapy with Reid.</p>
    </div>
    <div class="fold" style="left:281px"></div>
    <div class="fold" style="left:561px"></div>
  </section>

</div>
</body>
</html>
```